A DL (210mm wide x 100mm deep) layered .psd prepared for print ready CMYK 300 dpi for gloss paper.

Target Market(s)

Business People & young professionals – middle – high income earners.

Requirements
Must have
• Heading:
TOP Brunch (big and bold)
Traders Owners Partners (smaller underneath)

Text:
Everything about the TOP Brunch is TOP. The TOP Brunches are aimed at Traders, Owners and Partners and are designed to be an environment for where people Thrive, Offer and Prosper, while learning Trade, Openness and Prudence.

These events will be held on Friday mornings at 7am on February 17, May 18, August 17 and November 16, 2012.

The Velvet Playhouse, 412 Marlow Lane, Newcastle.
For more information, Phone (02) 4813 5062 or email info@chapel365.example

Please include:
SFP Logo, Chapel365 Logo, & TOP Logo
Nice to have
• Open to blue colours refer to steadyfundplanning.example and Chapel365.example

- Open to graphics/illustrations/photos - Can also purchase images from PixVault.
Should not have
• Too Much Bright Red or Yellow (open to some but not like a Burgertown flyer)

```html
<!DOCTYPE html>
<html lang="en">
<head>
<meta charset="utf-8">
<title>TOP Brunch 2012</title>
<link href="https://fonts.googleapis.com/css2?family=Oswald:wght@500;700&family=Arimo:wght@400;700&display=swap" rel="stylesheet">
<style>
:root{
  --sky:#eaf3fb;
  --blue-light:#2f86d6;
  --blue:#1b67b8;
  --blue-deep:#0f4f98;
  --ice:#cfe9ff;
  --white:#ffffff;
  --ink:#454a50;
  --logo-blue:#1d5ea8;
  --logo-navy:#163d6e;
}
*{box-sizing:border-box;margin:0;padding:0}
html,body{width:1200px;height:2444px;overflow:hidden}
body{background:var(--white);font-family:"Arimo",Arial,sans-serif}
.flyer{position:relative;width:1200px;height:2444px;overflow:hidden;background:linear-gradient(180deg,var(--sky) 0,#ffffff 300px)}
.hero-photo{position:absolute;left:0;top:240px;width:1200px;height:830px;
  background:
    linear-gradient(180deg,rgba(255,255,255,0) 55%,rgba(200,190,175,.55) 78%,rgba(150,140,130,.6) 100%),
    linear-gradient(90deg,#b9c2cc 0,#e9ecef 22%,#f6f7f8 45%,#e3e7eb 65%,#f2f4f6 82%,#c7ced6 100%)}
.masthead{position:absolute;left:96px;top:86px;width:1016px;height:306px;border:5px solid rgba(255,255,255,.9);border-radius:18px;
  background:linear-gradient(180deg,#3d9ae6 0,var(--blue) 55%,var(--blue-deep) 100%);
  box-shadow:0 8px 22px rgba(10,50,100,.35);text-align:center;color:var(--white);z-index:3}
.masthead-title{font-family:"Oswald",Arial,sans-serif;font-weight:700;font-size:132px;line-height:1;margin-top:22px;letter-spacing:2px}
.masthead-sub{font-family:"Oswald",Arial,sans-serif;font-weight:500;font-size:66px;line-height:1;margin-top:16px}
.year-tag{position:absolute;left:848px;top:944px;width:336px;height:108px;border:4px solid var(--white);border-radius:12px;
  background:linear-gradient(180deg,#3a95e2,var(--blue-deep));color:var(--white);font-family:"Arimo",Arial,sans-serif;
  font-weight:400;font-size:76px;line-height:100px;text-align:center;z-index:3}
.info-panel{position:absolute;left:0;top:1052px;width:1200px;height:960px;
  background:linear-gradient(180deg,var(--blue-light) 0,var(--blue) 60%,var(--blue-deep) 100%)}
.panel-curve{position:absolute;left:0;top:1860px;width:1200px;height:160px}
.intro{position:absolute;left:160px;top:1112px;width:940px;color:var(--white);font-weight:700;font-size:45px;line-height:80px;text-align:justify}
.event-chevron{position:absolute;left:150px;top:1712px;width:56px;height:156px}
.event-dates{position:absolute;left:320px;top:1712px;width:800px;color:var(--ice);font-weight:700;font-size:39px;line-height:50px}
.venue{position:absolute;left:60px;top:2030px;width:1080px;text-align:center;color:var(--ink);font-weight:700;font-size:37px;line-height:52px;font-style:normal}
.sponsors{position:absolute;left:0;top:2220px;width:1200px;height:180px}
.sponsor{position:absolute;top:40px;font-family:"Arimo",Arial,sans-serif;font-weight:700;font-size:72px;line-height:100px;text-align:center}
.sponsor-top{left:70px;width:220px;color:var(--logo-navy)}
.sponsor-chapel{left:350px;width:400px;color:var(--logo-blue)}
.sponsor-sfp{left:800px;width:320px;color:var(--logo-blue)}
</style>
</head>
<body>
<main class="flyer">
  <div class="hero-photo" role="img" aria-label="Photo of young business professionals in light shirts and grey suits seated around a meeting table with laptops and coffee"></div>

  <header class="masthead">
    <h1 class="masthead-title">TOP BRUNCH</h1>
    <p class="masthead-sub">Traders Owners Partners</p>
  </header>

  <div class="year-tag">2012</div>

  <section class="info-panel"></section>
  <svg class="panel-curve" viewBox="0 0 1200 160" preserveAspectRatio="none" aria-hidden="true">
    <path d="M0 40 C300 120 700 30 1200 70 L1200 160 L0 160 Z" fill="#ffffff"/>
  </svg>

  <p class="intro">Everything about the TOP Brunch is TOP. The TOP Brunches are aimed at Traders, Owners and Partners and are designed to be an environment for where people Thrive, Offer and Prosper, while learning Trade, Openness and Prudence.</p>

  <svg class="event-chevron" viewBox="0 0 56 156" aria-hidden="true">
    <path d="M4 6 L28 6 L52 78 L28 150 L4 150 L28 78 Z" fill="#cfe9ff"/>
  </svg>
  <p class="event-dates">These events will be held on<br>Friday mornings at 7am on February 17,<br>May 18, August 17 and November 16, 2012.</p>

  <address class="venue">The Velvet Playhouse, 412 Marlow Lane, Newcastle.<br>For more information, Phone (02) 4813 5062 or email<br>info@chapel365.example</address>

  <footer class="sponsors">
    <div class="sponsor sponsor-top">TOP</div>
    <div class="sponsor sponsor-chapel">Chapel365</div>
    <div class="sponsor sponsor-sfp">SFP</div>
  </footer>
</main>
</body>
</html>
```